Email Signature

I would like an email signature that includes all 5 of my companies.

At the moment I just have a list of all 5 companies but that is too dull. Naturally, I would like it to be not too big but to clearly show all 5 companies.

Thanks

```html
<!DOCTYPE html>
<html lang="en">
<head>
<meta charset="utf-8">
<title>Email Signature – Varnelli Group</title>
<link href="https://fonts.googleapis.com/css2?family=Open+Sans:ital,wght@0,400;0,600;0,700;0,800;1,700&display=swap" rel="stylesheet">
<style>
  :root {
    --stage: #2b3337;
    --label: #ffffff;
    --sky-top: #cde9f7;
    --sky-bottom: #f4fafd;
    --skyline-light: #9ea1ad;
    --skyline-dark: #5b5d6b;
    --band: #5b5d6b;
    --band-text: #ffffff;
    --ink: #1b1b1b;
    --logo-grey: #6c6f78;
    --logo-green: #8cc65a;
    --logo-blue: #6fa3dc;
    --figure-top: #f2c330;
    --figure-bottom: #3b78c4;
  }
  * { box-sizing: border-box; margin: 0; padding: 0; }
  html, body { width: 1200px; height: 800px; overflow: hidden; }
  body {
    background: var(--stage);
    font-family: "Open Sans", Arial, sans-serif;
    position: relative;
  }
  .option-label {
    position: absolute; left: 0; width: 1200px; text-align: center;
    color: var(--label); font-size: 34px; font-weight: 400; line-height: 46px;
  }
  .option-label.first { top: 25px; }
  .option-label.second { top: 396px; }

  .signature {
    position: absolute; left: 45px; width: 1110px; height: 256px;
    background: linear-gradient(to bottom, var(--sky-top), var(--sky-bottom) 70%);
    overflow: hidden;
  }
  .signature.first { top: 82px; }
  .signature.second { top: 462px; }

  .skyline {
    position: absolute; left: 0; width: 100%; top: 204px; height: 26px;
    background: linear-gradient(to bottom, var(--skyline-light), var(--skyline-dark));
  }
  .signature.second .skyline { top: 200px; height: 56px; }
  .address-band {
    position: absolute; left: 0; bottom: 0; width: 100%; height: 26px;
    background: var(--band); color: var(--band-text);
    font-size: 15px; text-align: center; line-height: 26px;
  }

  .mascot { position: absolute; top: 36px; width: 120px; }
  .mascot .figure {
    width: 92px; height: 100px; margin-left: 14px; border-radius: 10px;
    background: linear-gradient(to bottom, var(--figure-top), var(--figure-bottom));
  }
  .mascot .name {
    font-weight: 800; font-size: 19px; line-height: 24px; color: var(--ink);
    margin-top: 6px; white-space: nowrap;
  }
  .mascot.brace { left: 22px; }
  .mascot.rail { left: 282px; }
  .mascot.mend { left: 706px; }

  .brand { position: absolute; color: var(--logo-grey); font-weight: 700; line-height: 1; }
  .brand .dot { display: block; border-radius: 50%; margin-bottom: 8px; }
  .brand .tagline {
    display: block; font-size: 8px; font-weight: 400; margin-top: 5px;
  }
  .brand.structural { left: 146px; top: 36px; font-size: 25px; }
  .brand.structural .dot { width: 60px; height: 60px; background: var(--logo-green); margin-left: 10px; }
  .brand.sealant { left: 414px; top: 36px; font-size: 30px; }
  .brand.sealant .dot { width: 54px; height: 54px; background: var(--logo-blue); }

  .contact {
    position: absolute; font-size: 16px; color: var(--ink);
    line-height: 33px; white-space: nowrap;
  }
  .signature.first .contact { left: 861px; top: 48px; }
  .signature.second .contact { left: 892px; top: 56px; }
  .contact .lead { font-weight: 700; font-style: italic; }
  .contact .strong { font-weight: 700; }
  .contact .key { font-weight: 700; font-style: italic; }
</style>
</head>
<body>
  <div class="option-label first">option -1</div>
  <section class="signature first">
    <div class="skyline" role="img" aria-label="City skyline silhouette"></div>
    <div class="mascot brace">
      <div class="figure" role="img" aria-label="Cartoon builder mascot holding a spanner beside scaffolding"></div>
      <div class="name">Mr. Brace</div>
    </div>
    <div class="brand structural"><span class="dot"></span>Varnelli<br>Structural<span class="tagline">A Varnelli Group Company</span></div>
    <div class="mascot rail">
      <div class="figure" role="img" aria-label="Cartoon builder mascot beside a fence panel"></div>
      <div class="name">Mr. Rail</div>
    </div>
    <div class="brand sealant"><span class="dot"></span>Summit Sealant<br>Services<span class="tagline">A Varnelli Group Company</span></div>
    <div class="mascot mend">
      <div class="figure" role="img" aria-label="Cartoon builder mascot with trowel and hawk"></div>
      <div class="name">Mr. Mend</div>
    </div>
    <div class="contact">
      <div class="lead">A Varnelli Group Company</div>
      <div><span class="key">ABN</span> 31 604 218 557</div>
      <div>Builder Licence BLD 208391</div>
    </div>
    <div class="address-band">PO Box 17, Harbourview SA 5062</div>
  </section>

  <div class="option-label second">option -2</div>
  <section class="signature second">
    <div class="skyline" role="img" aria-label="City skyline silhouette"></div>
    <div class="mascot brace">
      <div class="figure" role="img" aria-label="Cartoon builder mascot holding a spanner beside scaffolding"></div>
      <div class="name">Mr. Brace</div>
    </div>
    <div class="brand structural"><span class="dot"></span>Varnelli<br>Structural<span class="tagline">A Varnelli Group Company</span></div>
    <div class="mascot rail">
      <div class="figure" role="img" aria-label="Cartoon builder mascot beside a fence panel"></div>
      <div class="name">Mr. Rail</div>
    </div>
    <div class="brand sealant"><span class="dot"></span>Summit Sealant<br>Services<span class="tagline">A Varnelli Group Company</span></div>
    <div class="mascot mend">
      <div class="figure" role="img" aria-label="Cartoon builder mascot with trowel and hawk"></div>
      <div class="name">Mr. Mend</div>
    </div>
    <div class="contact">
      <div class="strong">Your Name, Designation</div>
      <div><span class="key">Phone :</span> 123-123-1234</div>
      <div><span class="key">ABN</span> 31 604 218 557</div>
    </div>
  </section>
</body>
</html>
```